Law Firm Stationery Design - Traditional Meets Intuitive

Looking for a modern, yet classic, law firm stationery design. Simplicity is desired, but great ideas are encouraged. See attachment for company information. We utilize a variety of non-traditional legal tools to bring a different perspective to each of our client's particular situation. Final design should communicate classic values with intuitive, unique solutions.

Industry/Entity Type

Law Firm

Requirements
Should not have
• - No typical legal icons
• - No Tag Line!
• - DO NOT WANT WHAT WE ALREADY HAVE

```html
<!DOCTYPE html>
<html lang="en">
<head>
<meta charset="utf-8">
<title>Clarion Law LLC – Business Card</title>
<link rel="stylesheet" href="https://fonts.googleapis.com/css2?family=Quicksand:wght@400;500&display=swap">
<style>
  :root {
    --backdrop: #161718;
    --paper: #f4f4f3;
    --ink: #2b2b2b;
    --brand-blue: #0e4a63;
    --brand-blue-deep: #042a3b;
    --bar-grey: #a3a3a3;
    --on-dark: #e8eef1;
  }
  * { margin: 0; padding: 0; box-sizing: border-box; }
  html, body {
    width: 1200px; height: 1001px; overflow: hidden;
    background: var(--backdrop);
    font-family: "Quicksand", sans-serif;
  }
  .canvas { position: relative; width: 1200px; height: 1001px; }

  .card {
    position: absolute; left: 306px; width: 589px; height: 330px;
    box-shadow: 0 3px 10px rgba(0,0,0,.5);
  }
  .card--front { top: 133px; background: var(--paper); }
  .card--back {
    top: 539px;
    background: linear-gradient(180deg, var(--brand-blue) 0%, #08384e 55%, var(--brand-blue-deep) 100%);
  }

  .accent-bar { position: absolute; top: 0; height: 11px; }
  .accent-bar--grey { left: 0; width: 314px; background: var(--bar-grey); }
  .accent-bar--blue { left: 324px; right: 0; background: var(--brand-blue); }

  .firm-name {
    position: absolute; left: 37px; top: 57px;
    font-size: 36px; font-weight: 400; letter-spacing: -1px;
    color: var(--brand-blue); line-height: 1;
  }
  .contact {
    position: absolute; left: 37px; top: 214px;
    font-size: 14.5px; line-height: 17.6px; color: var(--ink);
    font-style: normal;
  }
  .contact .tel { margin-left: 10px; }
  .person {
    position: absolute; right: 35px; top: 215px; text-align: right; color: var(--ink);
  }
  .person-name { font-size: 24px; font-weight: 400; letter-spacing: -.5px; line-height: 1.1; }
  .person-role { font-size: 14.5px; margin-top: 3px; }

  .back-name {
    position: absolute; left: 0; right: 0; top: 143px; text-align: center;
    font-size: 35px; letter-spacing: -1px; color: var(--on-dark); line-height: 1;
  }
  .back-web {
    position: absolute; left: 0; right: 0; top: 266px; text-align: center;
    font-size: 13.5px; color: #b9c9d1;
  }
</style>
</head>
<body>
<main class="canvas">
  <section class="card card--front">
    <div class="accent-bar accent-bar--grey"></div>
    <div class="accent-bar accent-bar--blue"></div>
    <h1 class="firm-name">CLARION LAW LLC</h1>
    <address class="contact">
      CLARION LAW LLC<br>
      18 Harbor Lane, Suite 300<br>
      Weston, MA 02493<span class="tel">Tel: 555-014-2200</span><br>
      www.clarionlaw.com
    </address>
    <div class="person">
      <div class="person-name">JORDAN ELLISON</div>
      <div class="person-role">General Manager</div>
    </div>
  </section>

  <section class="card card--back">
    <h2 class="back-name">CLARION LAW LLC</h2>
    <div class="back-web">www.clarionlaw.com</div>
  </section>
</main>
</body>
</html>
```